Business Podcaster needs a sexy book cover design for upcoming book launch

I'm launching a book called Find Your Mentor: how to accelerate your growth through reaching out, getting a response from, and leaving an impression on the people you admire most. It would be cool to have maybe a band of heroes or a single hero or something on the cover, then I'll need the spine designed, as well as the back cover which would be mostly just quotes about the book from other prominent people.

I dont want to extend it. I want to shorten it. Can I do that?

```html
<!DOCTYPE html>
<html lang="en">
<head>
<meta charset="utf-8">
<title>Find Your Mentor – Book Cover and Spine</title>
<link rel="stylesheet" href="https://fonts.googleapis.com/css2?family=Anton&family=Oswald:wght@500;700&display=swap">
<style>
  :root {
    --page-bg: #ffffff;
    --cover-red: #c43338;
    --cover-wine: #5a1a1c;
    --cover-black: #000000;
    --accent-orange: #ff9933;
    --accent-red: #ff0000;
    --arc-dark: #4e1517;
    --title-white: #ffffff;
    --glow-gold: #f3c255;
    --glow-amber: #e07a1f;
    --frame-gold: #d9b26c;
  }
  * { margin: 0; padding: 0; box-sizing: border-box; }
  html, body { width: 1200px; height: 1200px; overflow: hidden; background: var(--page-bg); }
  .canvas { position: relative; width: 1200px; height: 1200px; }

  .front-cover {
    position: absolute; left: 356px; top: 105px; width: 491px; height: 694px;
    overflow: hidden;
    background: linear-gradient(180deg, var(--cover-red) 0%, #8a2426 28%, var(--cover-wine) 46%, #1a0606 62%, var(--cover-black) 78%);
  }
  .corner-arcs { position: absolute; inset: 0; width: 491px; height: 694px; }

  .title-top, .title-main {
    position: absolute; left: 0; width: 100%; text-align: center;
    font-family: "Anton", "Oswald", sans-serif; line-height: 1;
  }
  .front-cover .title-top { top: 66px; font-size: 66px; letter-spacing: 12px; color: var(--title-white); padding-left: 12px; }
  .front-cover .title-main { top: 160px; font-size: 86px; letter-spacing: 8px; color: var(--accent-orange); padding-left: 8px; }

  .hero-figure {
    position: absolute; left: 16px; top: 284px; width: 176px; height: 448px;
    background: radial-gradient(circle at 50% 24%, var(--glow-gold) 0%, var(--glow-amber) 22%, #8e1a1a 42%, rgba(60,10,10,0) 70%);
    border-top-left-radius: 88px; border-top-right-radius: 88px;
  }
  .horizon-glow {
    position: absolute; left: 0; bottom: 0; width: 100%; height: 140px;
    background: radial-gradient(ellipse at 32% 18%, rgba(255,214,110,0.9) 0%, rgba(214,120,30,0.5) 18%, rgba(30,40,60,0.6) 42%, rgba(0,0,0,0) 72%);
  }

  .subtitle {
    position: absolute; left: 208px; top: 395px; width: 242px;
    font-family: "Oswald", "Anton", sans-serif; font-weight: 700;
    font-size: 19px; line-height: 25.5px; color: var(--title-white);
    text-align: justify; text-align-last: justify;
  }
  .author-name {
    position: absolute; left: 0; top: 634px; width: 100%; text-align: center;
    font-family: "Oswald", sans-serif; font-weight: 700; font-size: 21px;
    color: var(--title-white); letter-spacing: -0.3px;
  }

  .thumb-cover {
    position: absolute; left: 590px; top: 899px; width: 490px; height: 301px;
    background: linear-gradient(180deg, var(--cover-red) 0%, #9a2829 45%, var(--cover-wine) 100%);
  }
  .thumb-cover .title-top { top: 38px; font-size: 66px; letter-spacing: 12px; color: var(--title-white); padding-left: 12px; }
  .thumb-cover .title-main { top: 128px; font-size: 84px; letter-spacing: 8px; color: var(--accent-orange); padding-left: 8px; }

  .spine {
    position: absolute; left: 1080px; top: 899px; width: 54px; height: 301px;
    background: var(--cover-black);
    display: flex; justify-content: center; padding-top: 36px;
  }
  .spine-title {
    writing-mode: vertical-rl;
    font-family: "Anton", sans-serif; font-size: 34px; line-height: 1;
    color: var(--title-white); white-space: nowrap; letter-spacing: -0.5px;
  }
</style>
</head>
<body>
<main class="canvas">
  <section class="front-cover">
    <svg class="corner-arcs" viewBox="0 0 491 694" aria-hidden="true">
      <path d="M60 0 C 260 10, 420 110, 491 245 L 491 0 Z" fill="var(--arc-dark)"/>
      <path d="M200 0 C 330 10, 440 70, 491 140 L 491 0 Z" fill="var(--accent-orange)"/>
      <path d="M250 0 C 350 8, 440 40, 491 92 L 491 0 Z" fill="var(--accent-red)"/>
    </svg>
    <h1 class="title-top">FIND YOUR</h1>
    <p class="title-main">MENTOR</p>
    <div class="horizon-glow" role="img" aria-label="Sunrise glowing over the curve of a planet"></div>
    <div class="hero-figure" role="img" aria-label="Silhouette of a businessman standing with folded arms before a gold-framed sunset disc"></div>
    <p class="subtitle">... How to accelerate your growth through reaching out, getting a response from, and leaving an impression on the people you admire most.</p>
    <p class="author-name">Author Name</p>
  </section>

  <section class="thumb-cover">
    <p class="title-top">FIND YOUR</p>
    <p class="title-main">MENTOR</p>
  </section>
  <aside class="spine">
    <span class="spine-title">FIND YOUR MENTOR</span>
  </aside>
</main>
</body>
</html>
```